Brackenford Group Website

We have a newly established brand for a company with an existing portfolio of property. The company is corporate and professional and both owns and develops property. The website should reflect a professional and stable organisation. The website should showcase the existing properties (6), have a home page that describes the company and its activities and has a "about us" page. The website will be in Wordpress and we would like the code for all pages to be sent to us by the successful designer upon completion of the job.
Updates

sorry was called from the office on an urgent matter. To be fair on submitters, i need a couple more days to finalise reviews.

Contact Information for Business Card

Brackenford Logo on front
Black background with silver logo.

Coding

Number of Pages Required

Colors

Designer to choose colors to be used in the design.

Requirements
Must have
• Text side of card should include
• Brackenford Property Group (as title in logo font)
• Employee Name (centered)
• Job Title (centered below name)
• Address 4 lines
• Email, mobile office phone, 3 lines
• website address (probably as footer)

```html
<!DOCTYPE html>
<html lang="en">
<head>
<meta charset="utf-8">
<title>Brackenford Group</title>
<link rel="stylesheet" href="https://fonts.googleapis.com/css2?family=Lato:wght@300;400;700&family=Playfair+Display:wght@400;700&display=swap">
<style>
:root{
  --navy:#0d1a3d;
  --yellow:#f7e81c;
  --ink:#222;
  --muted:#555;
  --dark:#2b2b2b;
  --darker:#1f1f1f;
  --light-text:#d8d8d8;
  --white:#fff;
  --serif:'Playfair Display',Georgia,serif;
  --sans:'Lato',Helvetica,Arial,sans-serif;
}
*{margin:0;padding:0;box-sizing:border-box}
html,body{width:1200px;height:4103px;overflow:hidden}
body{position:relative;background:var(--white);font-family:var(--sans);color:var(--ink)}
.abs{position:absolute}

.hero{position:absolute;left:0;top:0;width:1200px;height:576px;background:linear-gradient(180deg,#0b1533 0%,#142454 45%,#1a2238 75%,#0d0f1a 100%)}
.logo{position:absolute;left:96px;top:58px;display:flex;align-items:center;gap:10px;font-family:var(--serif);font-size:22px;color:#d9dde6;letter-spacing:1px}
.logo-mark{width:16px;height:16px;border:1px solid #d9dde6}
.nav{position:absolute;top:36px;left:0;width:1200px;font-size:11px;color:var(--white);letter-spacing:.3px}
.nav span{position:absolute}
.hero h1{position:absolute;left:92px;top:212px;font-family:var(--serif);font-weight:700;font-size:50px;color:var(--white);white-space:nowrap}
.hero p{position:absolute;left:92px;top:280px;font-family:var(--serif);font-size:21px;line-height:31px;color:var(--white);white-space:nowrap}
.btn-yellow{position:absolute;left:93px;top:363px;width:140px;height:38px;background:var(--yellow);font-size:11px;font-weight:700;letter-spacing:.5px;display:flex;align-items:center;justify-content:center;color:#111}
.slide-count{position:absolute;left:942px;top:494px;font-size:12px;color:var(--white)}
.slide-track{position:absolute;left:942px;top:520px;width:163px;height:2px;background:rgba(255,255,255,.35)}
.slide-track i{display:block;width:60px;height:3px;background:var(--yellow)}

.btn-outline{position:absolute;height:38px;border:2px solid #222;font-size:11px;font-weight:700;letter-spacing:.5px;display:flex;align-items:center;justify-content:center;color:#222}

.h2{position:absolute;font-family:var(--serif);font-size:56px;font-weight:400;color:#222}
.body-copy{position:absolute;font-size:13px;line-height:23.5px;color:var(--muted);font-weight:300;white-space:nowrap}
.photo{position:absolute}
.arrow-btn{position:absolute;width:40px;height:40px;display:flex;align-items:center;justify-content:center}
.arrow-dark{background:rgba(0,0,0,.55)}
.arrow-yellow{background:var(--yellow)}

.cases{position:absolute;left:0;top:1529px;width:1200px;height:1268px;background:var(--dark)}
.cases h2{position:absolute;top:46px;width:1200px;text-align:center;font-family:var(--serif);font-size:58px;font-weight:400;color:var(--white)}
.case{position:absolute;width:322px}
.case h3{font-family:var(--serif);font-weight:400;font-size:24px;color:var(--white);margin-bottom:6px}
.case p{font-size:15.5px;line-height:23.5px;color:var(--light-text);font-weight:300;padding-left:2px;height:118px;white-space:nowrap}
.case .go{width:26px;height:26px;border:1.5px solid var(--white);border-radius:50%;display:flex;align-items:center;justify-content:center;margin-left:2px}
.case .shot{margin-top:10px;width:322px;height:298px}

.member-photo{position:absolute;width:264px;height:180px}
.member-card{position:absolute;top:3073px;width:243px;height:163px;background:var(--white);box-shadow:0 2px 8px rgba(0,0,0,.15);padding:14px 12px}
.member-card h4{font-family:var(--serif);font-weight:400;font-size:20px;color:#222;white-space:nowrap}
.member-card .role{font-family:var(--serif);font-size:10.5px;color:#666;white-space:nowrap}
.member-card .summary{font-size:13px;line-height:19px;color:var(--muted);margin-top:8px;height:44px}
.member-card .follow{display:flex;align-items:center;gap:8px;font-size:12px;color:#777;margin-top:10px}
.member-card .follow i{display:block;width:22px;height:22px;background:#222}

.tile{position:absolute;width:338px;height:216px}

.footer{position:absolute;left:0;top:3771px;width:1200px;height:290px;background:var(--dark);color:#bbb;font-size:11px;line-height:17px}
.footer h5{font-family:var(--serif);font-weight:700;font-size:12px;letter-spacing:.5px;color:#eee;position:absolute}
.footer .col{position:absolute}
.footer .links div{margin-bottom:16px}
.footbar{position:absolute;left:0;top:4061px;width:1200px;height:42px;background:var(--darker);font-size:11px;color:#999;display:flex;align-items:center;justify-content:center}
.footbar b{font-weight:400;color:#eee;margin:0 3px}
</style>
</head>
<body>

<header class="hero" role="img" aria-label="Night city skyline of office towers">
  <div class="logo"><span class="logo-mark"></span>Brackenford</div>
  <nav class="nav">
    <span style="left:703px">ABOUT</span>
    <span style="left:776px">EXPERTISE</span>
    <span style="left:866px">CASE STUDIES</span>
    <span style="left:975px">TEAM</span>
    <span style="left:1041px">CONTACT US</span>
  </nav>
  <h1>Brackenford Group is a</h1>
  <p>Privately-Ownedcommercial real estate investment<br>Company founded in Auckland in 2007</p>
  <div class="btn-yellow">READ MORE</div>
  <div class="slide-count">1/3</div>
  <div class="slide-track"><i></i></div>
</header>

<section class="about">
  <h2 class="h2" style="left:97px;top:646px">About Us</h2>
  <p class="body-copy" style="left:97px;top:723px">Brackenford Group is a privately-owned commercial real estate investment<br>company founded in Auckland in 2007. Working with a small group of<br>long-standing private and institutional partners, the firm has successfully<br>acquired and developed assets valued at over $1.0 billion.</p>
  <div class="btn-outline" style="left:97px;top:840px;width:138px">READ MORE</div>
  <div class="photo" style="left:568px;top:623px;width:539px;height:303px;background:linear-gradient(160deg,#b9c2cc 0%,#6f7884 40%,#2a2f36 70%,#aab3bd 100%)" role="img" aria-label="Looking up at a dark glass office tower"></div>
</section>

<section class="expertise">
  <div class="photo" style="left:93px;top:995px;width:507px;height:476px;background:linear-gradient(170deg,#6d86b8 0%,#a5aebd 35%,#6a5a48 70%,#3a3024 100%)" role="img" aria-label="Residential towers at dusk with street lights"></div>
  <div class="arrow-btn arrow-dark" style="left:93px;top:1213px"><svg width="12" height="16"><path d="M9 2 3 8l6 6" stroke="#fff" stroke-width="2" fill="none"/></svg></div>
  <div class="arrow-btn arrow-yellow" style="left:560px;top:1213px"><svg width="12" height="16"><path d="M3 2l6 6-6 6" stroke="#111" stroke-width="2" fill="none"/></svg></div>
  <h2 class="h2" style="left:649px;top:980px">Expertise</h2>
  <h3 class="abs" style="left:649px;top:1094px;font-family:var(--serif);font-weight:400;font-size:25px">Acquisitions</h3>
  <p class="body-copy" style="left:649px;top:1138px">Prior to any successful real estate acquisition we plan and implement<br>proactive and thoughtful market and asset research. The Brackenford team<br>prides itself on our ability to evaluate market opportunities before others<br>see them. We use our longstanding relationships with the brokerage and<br>broader real estate community together with our reputation for "delivering<br>on our promises" to purchase and position unique investment<br>opportunities.</p>
  <div class="btn-outline" style="left:649px;top:1324px;width:162px;height:40px">VIEW ALL EXPERTISE</div>
</section>

<section class="cases">
  <h2>Case Studies</h2>
  <div class="case" style="left:93px;top:160px">
    <h3>Ashcombe</h3>
    <p>Ashcombe. 48 Harbour Av, Auckland CBD<br>The vision. The building was a run-down<br>backpacker lodge with a low earthquake<br>rating.</p>
    <div class="go"><svg width="10" height="12"><path d="M3 2l4 4-4 4" stroke="#fff" stroke-width="1.6" fill="none"/></svg></div>
    <div class="shot" style="background:linear-gradient(150deg,#cfe2f5 0%,#4d8ed0 45%,#1a4f8a 100%)" role="img" aria-label="Blue glass towers against the sky"></div>
  </div>
  <div class="case" style="left:438px;top:160px">
    <h3>The Halvern</h3>
    <p>Lorem ipsum dolor sit amet, consectetur<br>adipiscing elit. Pellentesque convallis mauris<br>non malesuada porttitor. Donec diam nunc,<br>semper</p>
    <div class="go"><svg width="10" height="12"><path d="M3 2l4 4-4 4" stroke="#fff" stroke-width="1.6" fill="none"/></svg></div>
    <div class="shot" style="background:linear-gradient(180deg,#c9d6e8 0%,#5b7bb0 50%,#1c2f5a 100%)" role="img" aria-label="Dark blue skyscraper seen from below"></div>
  </div>
  <div class="case" style="left:785px;top:160px">
    <h3>Dunmore</h3>
    <p>Lorem ipsum dolor sit amet, consectetur<br>adipiscing elit. Pellentesque convallis mauris<br>non malesuada porttitor. Donec diam nunc,<br>semper</p>
    <div class="go"><svg width="10" height="12"><path d="M3 2l4 4-4 4" stroke="#fff" stroke-width="1.6" fill="none"/></svg></div>
    <div class="shot" style="background:linear-gradient(160deg,#e3e8ed 0%,#7f919f 50%,#2c3a46 100%)" role="img" aria-label="Grey glass tower rising upward"></div>
  </div>
  <div class="case" style="left:93px;top:712px">
    <h3>Fernleigh</h3>
    <p>Ashcombe. 48 Harbour Av, Auckland CBD<br>The vision. The building was a run-down<br>backpacker lodge with a low earthquake<br>rating.</p>
    <div class="go"><svg width="10" height="12"><path d="M3 2l4 4-4 4" stroke="#fff" stroke-width="1.6" fill="none"/></svg></div>
    <div class="shot" style="background:linear-gradient(160deg,#9fc3e6 0%,#6a8fb2 50%,#34465a 100%)" role="img" aria-label="Angular apartment block against blue sky"></div>
  </div>
  <div class="case" style="left:438px;top:712px">
    <h3>Meridian</h3>
    <p>Lorem ipsum dolor sit amet, consectetur<br>adipiscing elit. Pellentesque convallis mauris<br>non malesuada porttitor. Donec diam nunc,<br>semper</p>
    <div class="go"><svg width="10" height="12"><path d="M3 2l4 4-4 4" stroke="#fff" stroke-width="1.6" fill="none"/></svg></div>
    <div class="shot" style="background:linear-gradient(150deg,#d8ecfa 0%,#3a8ad8 50%,#1458a8 100%)" role="img" aria-label="Glass curtain wall of a modern building"></div>
  </div>
  <div class="case" style="left:785px;top:712px">
    <h3>Six Twelve</h3>
    <p>Lorem ipsum dolor sit amet, consectetur<br>adipiscing elit. Pellentesque convallis mauris<br>non malesuada porttitor. Donec diam nunc,<br>semper</p>
    <div class="go"><svg width="10" height="12"><path d="M3 2l4 4-4 4" stroke="#fff" stroke-width="1.6" fill="none"/></svg></div>
    <div class="shot" style="background:linear-gradient(170deg,#3f6f94 0%,#7fa8c6 50%,#c7d8e4 100%)" role="img" aria-label="Curved glass tower reflecting clouds"></div>
  </div>
</section>

<section class="team">
  <h2 class="h2" style="left:93px;top:2998px">Team</h2>
  <div class="member-photo" style="left:274px;top:2893px;background:linear-gradient(135deg,#2a3f9a 0%,#3550b8 60%,#1a2660 100%)" role="img" aria-label="Portrait of Martin Hollis"></div>
  <div class="member-photo" style="left:558px;top:2893px;background:linear-gradient(135deg,#8a8a8a 0%,#6a6a6a 60%,#3a3a3a 100%)" role="img" aria-label="Portrait of Peter Lanford-Grey"></div>
  <div class="member-photo" style="left:841px;top:2893px;background:linear-gradient(135deg,#e8ecef 0%,#c7ced4 60%,#8c949b 100%)" role="img" aria-label="Portrait of Adam Rowe"></div>
  <div class="arrow-btn arrow-dark" style="left:278px;top:3003px"><svg width="12" height="16"><path d="M9 2 3 8l6 6" stroke="#fff" stroke-width="2" fill="none"/></svg></div>
  <div class="arrow-btn arrow-yellow" style="left:1067px;top:3003px"><svg width="12" height="16"><path d="M3 2l6 6-6 6" stroke="#111" stroke-width="2" fill="none"/></svg></div>

  <div class="member-card" style="left:285px">
    <h4>Martin Hollis</h4>
    <div class="role">(Senior Asset and Development Manager)</div>
    <div class="summary">20-30 word summary A leading<br>manager in the xxxxxxxx</div>
    <div class="follow">Follow <i></i></div>
  </div>
  <div class="member-card" style="left:569px">
    <h4>Peter Lanford-Grey</h4>
    <div class="role">(Director)</div>
    <div class="summary">Founder of Brackenford with many<br>years of asset and development</div>
    <div class="follow">Follow <i></i></div>
  </div>
  <div class="member-card" style="left:853px">
    <h4>Adam Rowe</h4>
    <div class="role">(Director)</div>
    <div class="summary">Praesent a tortor ut sapien<br>venenatis pretium ac eget lorem</div>
    <div class="follow">Follow <i></i></div>
  </div>
</section>

<section class="gallery">
  <div class="tile" style="left:93px;top:3296px;background:linear-gradient(160deg,#6f9cd6 0%,#9bb8dc 50%,#5a6a80 100%)" role="img" aria-label="Stepped white apartment building"></div>
  <div class="tile" style="left:431px;top:3296px;background:linear-gradient(160deg,#3a3a3e 0%,#242428 100%)" role="img" aria-label="Dark office tower, highlighted">
    <svg class="abs" style="left:139px;top:78px" width="60" height="60" viewBox="0 0 60 60" fill="none" stroke="#fff" stroke-width="2"><path d="M36 6h18v18M54 6 34 26M24 54H6V36M6 54l20-20"/></svg>
  </div>
  <div class="tile" style="left:769px;top:3296px;background:linear-gradient(160deg,#6fc6d6 0%,#2f8aa0 50%,#1e4c5a 100%)" role="img" aria-label="Teal glass towers from below"></div>
  <div class="tile" style="left:93px;top:3512px;background:linear-gradient(180deg,#8fb6e0 0%,#9aa6b3 55%,#5b7a4a 80%,#9a8f82 100%)" role="img" aria-label="City street with towers and trees"></div>
  <div class="tile" style="left:431px;top:3512px;background:linear-gradient(160deg,#4aa0e8 0%,#1c5fb0 50%,#0f3570 100%)" role="img" aria-label="Blue glass building corner"></div>
  <div class="tile" style="left:769px;top:3512px;background:linear-gradient(180deg,#b7c6d4 0%,#8e98a2 50%,#3e4146 100%)" role="img" aria-label="Low modern office block"></div>
</section>

<footer class="footer">
  <h5 style="left:95px;top:54px">CONTACT US</h5>
  <div class="col" style="left:95px;top:80px;display:flex;gap:8px">
    <svg width="10" height="14" viewBox="0 0 10 14"><path d="M5 0a5 5 0 0 0-5 5c0 4 5 9 5 9s5-5 5-9a5 5 0 0 0-5-5zm0 7a2 2 0 1 1 0-4 2 2 0 0 1 0 4z" fill="#bbb"/></svg>
    <div>Brackenford Group Ltd<br>Level 4, Kestrel House<br>12 Kestrel Lane<br>Auckland CBD<br>PO Box 2047<br>Harbour St<br>Auckland 1140</div>
  </div>
  <div class="col" style="left:270px;top:80px;display:flex;gap:8px;align-items:center">
    <svg width="12" height="12" viewBox="0 0 12 12"><path d="M2.5 0 5 3 3.5 4.5a8 8 0 0 0 4 4L9 7l3 2.5-1.5 2C5 11.5.5 7 .5 1.5z" fill="#bbb"/></svg>+64 9 555 0148
  </div>
  <div class="col" style="left:270px;top:112px;display:flex;gap:8px;align-items:center">
    <svg width="13" height="9" viewBox="0 0 13 9"><rect x=".5" y=".5" width="12" height="8" fill="none" stroke="#bbb"/><path d="M.5.5l6 4.5 6-4.5" stroke="#bbb" fill="none"/></svg>info@brackenfordgroup.example
  </div>
  <h5 style="left:268px;top:157px">FOLLOW US</h5>
  <div class="abs" style="left:270px;top:183px;width:24px;height:24px;border-radius:50%;background:#555"></div>

  <h5 style="left:569px;top:54px">QUICK LINKS</h5>
  <div class="col links" style="left:569px;top:86px">
    <div>About</div><div>Expertise</div><div>Case Studies</div><div>Team</div><div>Contact Us</div>
  </div>

  <h5 style="left:815px;top:54px">EXPERTISE</h5>
  <div class="col" style="left:815px;top:86px;width:160px">
    <div style="margin-bottom:16px">Acquisitions</div>
    <div style="margin-bottom:16px">Resource Management<br>Planning and Consenting</div>
    <div style="margin-bottom:16px">Development</div>
    <div>Renovation and Repositioning</div>
  </div>
  <div class="col" style="left:998px;top:86px;width:120px">
    <div style="margin-bottom:16px">Leasing and Asset<br>Management</div>
    <div>Financial Management</div>
  </div>
</footer>
<div class="footbar">© 2019 <b>Brackenford Property Group</b>. All Right Reserved.</div>

</body>
</html>
```